Popup Nightclub Grand Opening Flyer

We need to design a flyer for the grand opening of an upscale, exclusive nightclub called "Lanternfall". The design needs to be chic and exclusive. The background should be black and the text should primarily be white. We like minimalist designs.

Here is the text for the flyer
-
Velvetroom Atlanta Presents

Lanternfall (LOGO)

A Popup Nightclub Experience
For one night Only

Friday, October 18, 2013
Party begins at 9PM

INVITE ONLY

See invitation for location details
(Velvetroom Atlanta logo)

-
Examples we like

http://cdn2-b.plorvex-news.test/sites/default/files/styles/image_content_width/hash/3d/fb/4729105836_5521_flyer.jpg?itok=Q8rmZt2w

http://api.trevlomesh.test/files/9Kxq-Tr72PQd0hzXbwaLr8VMN2K617J3nqBw5CHR4XtdM8Y2sqEA-KjuxBnRoLW4QTyMHD8nwfYcJz-Rkh3vqp4MNaTYe9s1/7zenFridays.jpg

http://brenquist.test/wp-content/uploads/yootheme/widgetkit/gallery/7zen/7zen-gen_nvibe4-01.jpg
Updates

Hi All, one thing that we are seeing that we don't like is on over emphasis on the phrase "a popup nightclub experience" please don't make this the largest thing on the flyer

Target Market(s)

Target market is 25-35 year olds who are affluent (rich) and like luxury brands

Requirements
Must have
• Dark Background
Nice to have
• Velvetroom Logo on the bottom
Modern text that isn't curvy
Should not have
• Curved text

```html
<!DOCTYPE html>
<html lang="en">
<head>
<meta charset="utf-8">
<title>Lanternfall Nightclub – Velvetroom Atlanta</title>
<link rel="stylesheet" href="https://fonts.googleapis.com/css2?family=Josefin+Sans:ital,wght@0,100;0,300;0,400;0,700;1,400&family=Poiret+One&family=Graduate&display=swap">
<style>
  :root {
    --bg: #000000;
    --ink: #ffffff;
    --muted: #d6d6d6;
    --silver-light: #f2f2f2;
    --silver-dark: #8c8c8c;
  }
  * { margin: 0; padding: 0; box-sizing: border-box; }
  html, body { width: 816px; height: 1200px; overflow: hidden; background: var(--bg); }
  .flyer {
    position: relative;
    width: 816px;
    height: 1200px;
    background: var(--bg);
    color: var(--ink);
    font-family: "Josefin Sans", sans-serif;
    text-align: center;
  }
  .flyer > * { position: absolute; left: 0; width: 100%; }

  .presenter {
    top: 62px;
    font-family: "Josefin Sans", sans-serif;
    font-weight: 400;
    font-size: 21px;
    letter-spacing: 1px;
    color: var(--muted);
  }
  .presenter small { font-size: 15px; }

  .club-mark {
    top: 190px;
    left: 333px;
    width: 150px;
    height: 150px;
    border-radius: 50%;
    background: linear-gradient(180deg, var(--silver-light), var(--silver-dark));
  }
  .club-name {
    top: 452px;
    font-family: "Josefin Sans", sans-serif;
    font-weight: 300;
    font-size: 56px;
    letter-spacing: 8px;
    padding-left: 8px;
  }
  .club-type {
    top: 534px;
    font-family: "Josefin Sans", sans-serif;
    font-weight: 300;
    font-size: 32px;
    letter-spacing: 3px;
  }

  .tagline {
    top: 672px;
    font-family: "Poiret One", sans-serif;
    font-size: 41px;
    letter-spacing: 1px;
  }
  .tagline-band {
    top: 741px;
    height: 36px;
    background: var(--ink);
  }
  .headline {
    top: 734px;
    font-family: "Graduate", serif;
    font-size: 42px;
    letter-spacing: 2px;
    color: var(--ink);
    -webkit-text-stroke: 2px var(--bg);
    paint-order: stroke fill;
  }

  .event-date {
    top: 856px;
    left: 60px;
    width: 350px;
    font-family: "Poiret One", sans-serif;
    font-size: 26px;
    line-height: 34px;
    letter-spacing: 1px;
  }
  .event-date b { font-family: "Josefin Sans", sans-serif; font-weight: 700; }

  .access {
    top: 858px;
    left: 440px;
    width: 340px;
  }
  .access-title {
    font-family: "Graduate", serif;
    font-size: 30px;
    letter-spacing: 1px;
  }
  .access-note {
    margin-top: 6px;
    font-family: "Josefin Sans", sans-serif;
    font-style: italic;
    font-size: 13px;
    letter-spacing: 0.5px;
    text-transform: uppercase;
  }

  .host-brand {
    top: 1034px;
    display: flex;
    justify-content: center;
    align-items: center;
    gap: 16px;
  }
  .host-brand-dot {
    width: 34px;
    height: 34px;
    border-radius: 50%;
    background: var(--ink);
  }
  .host-brand-name {
    font-family: "Josefin Sans", sans-serif;
    font-weight: 400;
    font-size: 30px;
    letter-spacing: 3px;
    text-transform: uppercase;
  }
</style>
</head>
<body>
  <main class="flyer">
    <p class="presenter">VELVETROOM ATLANTA <small>PRESENTS:</small></p>

    <div class="club-mark" aria-hidden="true"></div>
    <h1 class="club-name">LANTERNFALL</h1>
    <p class="club-type">NIGHTCLUB</p>

    <p class="tagline">A POPUP NIGHTCLUB EXPERIENCE</p>
    <div class="tagline-band" aria-hidden="true"></div>
    <h2 class="headline">FOR ONE NIGHT ONLY</h2>

    <p class="event-date">FRIDAY, OCTOBER <b>18, 2013</b><br>PARTY BEGINS AT <b>9</b>PM</p>

    <div class="access">
      <p class="access-title">INVITE ONLY</p>
      <p class="access-note">See invitation for location details</p>
    </div>

    <div class="host-brand">
      <span class="host-brand-dot" aria-hidden="true"></span>
      <span class="host-brand-name">Velvetroom Atlanta</span>
    </div>
  </main>
</body>
</html>
```